New business card design

I need original, modern, business looking but dzen (minimalistic) looking design.
Also refer to websit trevanix.ru

Text is

Гордеев Степан, PMP
Партнер

Моб. +7 (915) 463 5817
info@trevanix.ru
Москва, Россия, 117356, ул. Берёзовая 7/2
=====================

Gordeev Stepan, PMP
Partner

Mob. +7 (915) 463 5817
info@trevanix.ru
Moscow, Russia,117356, Beryozovaya 7/2

```html
<!DOCTYPE html>
<html lang="en">
<head>
<meta charset="utf-8">
<title>Trevanix — Business Card</title>
<link href="https://fonts.googleapis.com/css2?family=Exo+2:wght@300;400;500;600&display=swap" rel="stylesheet">
<style>
  :root {
    --backdrop: #d6d7d8;
    --card: #ffffff;
    --ink: #333436;
    --accent-red: #8e2b2b;
    --panel-blue: #2b7cc3;
    --panel-line: rgba(255,255,255,0.85);
    --band: #3a3b3d;
    --brand: #2fa4d8;
    --on-blue: #ffffff;
  }
  * { box-sizing: border-box; margin: 0; padding: 0; }
  html, body {
    width: 1200px; height: 894px; overflow: hidden;
    background: var(--backdrop);
    font-family: "Exo 2", Arial, sans-serif;
  }
  .stage {
    position: relative; width: 1200px; height: 894px;
    display: flex; align-items: center; justify-content: center; gap: 60px;
  }
  .card {
    position: relative; width: 520px; height: 297px;
    background: var(--card);
    box-shadow: 0 6px 18px rgba(0,0,0,0.18);
    overflow: hidden;
  }
  .card__band {
    position: absolute; right: 0; top: 34px;
    width: 132px; height: 40px; background: var(--band);
  }
  .card--back .card__band { top: 18px; height: 34px; }
  /* front */
  .brand {
    position: absolute; left: 0; right: 0; top: 118px;
    display: flex; align-items: center; justify-content: center; gap: 14px;
  }
  .brand__mark { width: 40px; height: 40px; background: var(--brand); }
  .brand__name {
    font-size: 46px; font-weight: 300; color: var(--brand); letter-spacing: 1px;
  }
  /* back */
  .person {
    position: absolute; right: 24px; top: 64px; text-align: right;
  }
  .person__name {
    font-size: 24px; font-weight: 600; letter-spacing: 1.2px; text-transform: uppercase;
    color: var(--ink); line-height: 1; white-space: nowrap;
  }
  .person__name .first { color: var(--accent-red); }
  .person__role {
    margin-top: 8px; font-size: 15px; font-weight: 500; letter-spacing: 2px;
    text-transform: uppercase; color: var(--ink);
  }
  .contact-panel {
    position: absolute; left: 18px; right: 18px; top: 138px; bottom: 16px;
    background: var(--panel-blue); border-radius: 14px;
    display: grid; grid-template-columns: repeat(3, 1fr);
    color: var(--on-blue);
  }
  .contact {
    padding: 16px 10px 0; text-align: center;
    font-size: 12.5px; line-height: 1.5; letter-spacing: 0.6px;
  }
  .contact + .contact { border-left: 1.5px solid var(--panel-line); }
  .contact__icon { width: 30px; height: 30px; display: block; margin: 0 auto 12px; }
</style>
</head>
<body>
<main class="stage">
  <section class="card card--front" aria-label="Card front">
    <div class="card__band"></div>
    <div class="brand">
      <span class="brand__mark"></span>
      <span class="brand__name">Trevanix</span>
    </div>
  </section>

  <section class="card card--back" aria-label="Card back">
    <div class="card__band"></div>
    <div class="person">
      <p class="person__name"><span class="first">Gordeev</span> Stepan, PMP</p>
      <p class="person__role">Partner</p>
    </div>
    <div class="contact-panel">
      <div class="contact contact--phone">
        <svg class="contact__icon" viewBox="0 0 32 32" aria-hidden="true">
          <path fill="#fff" d="M4 11c0-3 5-5 12-5s12 2 12 5v2h-6v-2.5c-2-.6-4-.8-6-.8s-4 .2-6 .8V13H4z"/>
          <path fill="#fff" d="M9 14h14l4 9v4H5v-4z"/>
          <circle cx="16" cy="20" r="3" fill="#2b7cc3"/>
        </svg>
        <p>Mob.</p>
        <p>+7 (915) 463 5817</p>
      </div>
      <div class="contact contact--web">
        <svg class="contact__icon" viewBox="0 0 32 32" aria-hidden="true" fill="none" stroke="#fff" stroke-width="2">
          <circle cx="16" cy="16" r="12"/>
          <ellipse cx="16" cy="16" rx="5" ry="12"/>
          <path d="M4 16h24M6 10h20M6 22h20"/>
        </svg>
        <p>info@trevanix.ru</p>
        <p>trevanix.ru</p>
      </div>
      <div class="contact contact--address">
        <svg class="contact__icon" viewBox="0 0 32 32" aria-hidden="true">
          <path fill="#fff" d="M16 3a9 9 0 0 0-9 9c0 7 9 17 9 17s9-10 9-17a9 9 0 0 0-9-9z"/>
          <circle cx="16" cy="12" r="3.5" fill="#2b7cc3"/>
        </svg>
        <p>Beryozovaya 7/2</p>
        <p>Moscow, Russia, 117356</p>
      </div>
    </div>
  </section>
</main>
</body>
</html>
```